Freelance Writer Letterhead Design

I need business letterhead designed for my freelance public relations/writing company in Denver, Colorado. I write and create articles, white papers, blogs and enewsletters for trade associations, health care organizations and foundations. I already have three versions of my logo in three colors. I would like the design to be executed in the three different colors, so I can use them in various ways. The final design should communicate professionalism, creativity and intellectual work. I want clients to think, "She is smart, professional, creative and more polished than the typical freelance writer; she looks like an agency, but is an individual."

Target Market(s)

Healthcare consulting firms, Foundations,

Industry/Entity Type

Communications

Other font styles liked:
• Avenir.ttc and Outage.ttf are used in the logo

Requirements
Must have
• The logo
• I'd like it also to have as part of the design, these elements:
• Address: 4870 W. Linden Court, #215, Denver, CO 80231
• Website: www.quillmerewritingllc.com
• contact information: maude@quillmerewritingllc.com
• phone: 303-918-2045
Nice to have
• a band of color at the bottom or along the sides, using the logo colors

```html
<!DOCTYPE html>
<html lang="en">
<head>
<meta charset="utf-8">
<title>Quillmere Writing Letterhead</title>
<link rel="stylesheet" href="https://fonts.googleapis.com/css2?family=Arimo:wght@400;700&family=Nunito+Sans:wght@800&family=Source+Sans+3:wght@400&family=Pinyon+Script&display=swap">
<style>
  :root {
    --brand-green: #9cc93b;
    --ink: #1e1e1e;
    --body-grey: #5a5a5a;
    --sub-grey: #4a4a4a;
    --paper: #ffffff;
  }
  * { margin: 0; padding: 0; box-sizing: border-box; }
  html, body { width: 887px; height: 1200px; overflow: hidden; background: var(--paper); }
  .letterhead { position: relative; width: 887px; height: 1200px; background: var(--paper); }

  .top-band { position: absolute; left: 0; top: 0; width: 887px; height: 14px; background: var(--brand-green); }
  .top-tab { position: absolute; left: 62px; top: 0; width: 349px; height: 37px; background: var(--brand-green); }

  .brand { position: absolute; left: 62px; top: 104px; display: flex; align-items: center; gap: 14px; }
  .brand-dot { width: 46px; height: 46px; border-radius: 50%; background: var(--brand-green); }
  .brand-name { font-family: "Nunito Sans", sans-serif; font-weight: 800; font-size: 38px; color: var(--brand-green); letter-spacing: 0.5px; }

  .contact { position: absolute; right: 50px; top: 58px; list-style: none; font-family: Arimo, sans-serif; font-size: 15px; color: var(--ink); }
  .contact li { display: flex; align-items: flex-start; justify-content: flex-end; gap: 14px; height: 40px; }
  .contact li span { text-align: right; line-height: 20px; padding-top: 5px; }
  .contact svg { width: 30px; height: 30px; flex: none; }

  .headline { position: absolute; left: 62px; top: 330px; font-family: Arimo, sans-serif; font-weight: 400; font-size: 37px; color: var(--ink); }
  .headline em { font-style: normal; color: var(--brand-green); }
  .headline-rule { position: absolute; left: 62px; top: 372px; width: 390px; height: 3px; background: var(--brand-green); }
  .subhead { position: absolute; left: 62px; top: 386px; width: 420px; font-family: "Source Sans 3", sans-serif; font-size: 18px; line-height: 22px; color: var(--sub-grey); }

  .body-copy { position: absolute; left: 62px; width: 760px; font-family: "Source Sans 3", sans-serif; font-size: 14.5px; line-height: 24.5px; color: var(--body-grey); text-align: justify; letter-spacing: 0.4px; }
  .para-1 { top: 476px; }
  .para-2 { top: 680px; }
  .para-3 { top: 834px; }
  .section-rule { position: absolute; left: 238px; width: 330px; height: 3px; background: var(--brand-green); }
  .rule-1 { top: 664px; }
  .rule-2 { top: 820px; }

  .signature { position: absolute; left: 62px; top: 990px; font-family: "Pinyon Script", cursive; font-size: 34px; color: var(--sub-grey); border-bottom: 2px solid var(--sub-grey); line-height: 1.1; }

  .bottom-band { position: absolute; left: 0; bottom: 0; width: 887px; height: 18px; background: var(--brand-green); }
  .bottom-tab { position: absolute; left: 62px; bottom: 0; width: 349px; height: 40px; background: var(--brand-green); color: #fff; font-family: Arimo, sans-serif; font-weight: 700; font-size: 16px; display: flex; align-items: center; justify-content: center; padding-bottom: 4px; }
</style>
</head>
<body>
<main class="letterhead">
  <div class="top-band"></div>
  <div class="top-tab"></div>

  <div class="brand">
    <div class="brand-dot"></div>
    <div class="brand-name">Quillmere Writing</div>
  </div>

  <ul class="contact">
    <li><span>303-918-2045</span>
      <svg viewBox="0 0 30 30"><circle cx="15" cy="15" r="15" fill="#9cc93b"/><path d="M10.5 8.5l3 3-1.6 1.8c.9 1.9 2.4 3.4 4.3 4.3l1.8-1.6 3 3-2 2c-5 0-10.5-5.5-10.5-10.5z" fill="#fff"/></svg></li>
    <li><span>www.quillmerewritingllc.com</span>
      <svg viewBox="0 0 30 30"><circle cx="15" cy="15" r="15" fill="#9cc93b"/><g fill="none" stroke="#fff" stroke-width="1.5"><circle cx="15" cy="15" r="7"/><ellipse cx="15" cy="15" rx="3" ry="7"/><path d="M8 15h14"/></g></svg></li>
    <li><span>maude@quillmerewritingllc.com</span>
      <svg viewBox="0 0 30 30"><circle cx="15" cy="15" r="15" fill="#9cc93b"/><rect x="8.5" y="10" width="13" height="10" fill="#fff"/><path d="M8.5 10l6.5 5.5 6.5-5.5" fill="none" stroke="#9cc93b" stroke-width="1.4"/></svg></li>
    <li><span>4870 W. Linden Court, #215,<br>Denver, CO 80231</span>
      <svg viewBox="0 0 30 30"><circle cx="15" cy="15" r="15" fill="#9cc93b"/><path d="M15 23s-6-6.5-6-10.5a6 6 0 0 1 12 0c0 4-6 10.5-6 10.5z" fill="#fff"/><circle cx="15" cy="12.5" r="2.2" fill="#9cc93b"/></svg></li>
  </ul>

  <h1 class="headline">YOUR <em>HEADLINE</em></h1>
  <div class="headline-rule"></div>
  <p class="subhead">Lorem ipsum dolor sit amet, consectetuer adipiscing elit, sed diam</p>

  <p class="body-copy para-1">Lorem ipsum dolor sit amet, consectetuer adipiscing elit, sed diam nonummy nibh euismod tincidunt ut laoreet dolore magna aliquam erat volutpat. Ut wisi enim ad minim veniam, quis nostrud exerci tation ullamcorper suscipit lobortis nisl ut aliquip ex ea commodo consequat. Duis autem vel eum iriure dolor in hendrerit in vulputate velit esse molestie consequat, vel illum dolore eu feugiat nulla facilisis at vero eros et accumsan et iusto odio dignissim qui blandit praesent luptatum zzril delenit augue duis dolore te feugait nulla facilisi.</p>
  <div class="section-rule rule-1"></div>
  <p class="body-copy para-2">Nam liber tempor cum soluta nobis eleifend option congue nihil imperdiet doming id quod mazim placerat facer possim assum. Typi non habent claritatem insitam; est usus legentis in iis qui facit eorum claritatem. Investigationes demonstraverunt lectores legere me lius quod ii legunt saepius. Claritas est etiam processus dynamicus, qui sequitur mutationem consuetudium lectorum.</p>
  <div class="section-rule rule-2"></div>
  <p class="body-copy para-3">Mirum est notare quam littera gothica, quam nunc putamus parum claram, anteposuerit litterarum formas humanitatis per seacula quarta decima et quinta decima. Eodem modo typi, qui nunc nobis videntur parum clari, ant sollemnes in futurum.</p>

  <div class="signature">Signature</div>

  <div class="bottom-band"></div>
  <div class="bottom-tab">www.quillmerewritingllc.com</div>
</main>
</body>
</html>
```